Letterhead Design Needed for Real Estate Office

We are a boutique real estate agency focused on property management. We need a letter head which is professional looking and include the following information:

Logo
ABN Number
Address
Postal Address
Phone
Fax
Mobile
Email
Website

Please note that the PLVAQT logo can not be changed and must be positioned at the bottom right corner.

Please find attached the existing letterhead design for all the required elements.

Target Market(s)

Letterhead mostly used for service of notices, business letters, clients communication

Industry/Entity Type

Boutique

Colors

Designer to choose colors to be used in the design.

Requirements
Must have
• Logo

```html
<!DOCTYPE html>
<html lang="en">
<head>
<meta charset="utf-8">
<title>Northvale Partners — Letterhead</title>
<link rel="stylesheet" href="https://fonts.googleapis.com/css2?family=Lustria&display=swap">
<style>
  :root {
    --paper: #ffffff;
    --frame-green: #7cc242;
    --ink: #2b2b2b;
    --brand-ink: #3a3a3a;
    --brand-accent: #5e9e2c;
    --watermark: #e9eef5;
    --badge-ink: #2a4b7c;
  }
  html, body {
    margin: 0;
    padding: 0;
    overflow: hidden;
    background: var(--paper);
  }
  .letterhead {
    position: relative;
    width: 847px;
    height: 1200px;
    overflow: hidden;
    background: var(--paper);
    font-family: "Lustria", Georgia, serif;
    color: var(--ink);
  }
  .frame {
    position: absolute;
    inset: 0;
    width: 847px;
    height: 1200px;
  }
  .watermark {
    position: absolute;
    left: 62px;
    top: 205px;
    width: 748px;
    height: 760px;
    border-radius: 50%;
    background: radial-gradient(closest-side, var(--watermark) 0%, rgba(233,238,245,0.6) 55%, rgba(255,255,255,0) 100%);
  }
  .brand {
    position: absolute;
    left: 34px;
    top: 52px;
    display: flex;
    align-items: center;
    gap: 14px;
  }
  .brand-square {
    width: 58px;
    height: 58px;
    background: var(--brand-accent);
  }
  .brand-name {
    font-size: 30px;
    line-height: 1.05;
    color: var(--brand-ink);
    letter-spacing: 1px;
    text-transform: uppercase;
  }
  .contact {
    position: absolute;
    left: 524px;
    top: 22px;
    font-size: 18px;
    line-height: 23.6px;
    font-style: normal;
    margin: 0;
  }
  .contact-row {
    display: flex;
    margin: 0;
    white-space: nowrap;
  }
  .contact-label {
    width: 88px;
    flex: none;
  }
  .member-badge {
    position: absolute;
    left: 586px;
    top: 1000px;
    display: flex;
    align-items: center;
    gap: 12px;
  }
  .member-square {
    width: 40px;
    height: 40px;
    background: var(--badge-ink);
  }
  .member-name {
    font-size: 44px;
    color: var(--badge-ink);
    letter-spacing: 1px;
  }
</style>
</head>
<body>
<div class="letterhead">
  <svg class="frame" viewBox="0 0 847 1200" aria-hidden="true">
    <path fill="var(--frame-green)" fill-rule="evenodd"
      d="M0 0 H847 V1200 H0 Z
         M6 6 L833 16 L840 1194 L14 1186 Z"/>
  </svg>

  <div class="watermark" role="img" aria-label="Faint four-pointed star watermark decoration"></div>

  <header class="brand">
    <div class="brand-square"></div>
    <div class="brand-name">Northvale<br>Partners</div>
  </header>

  <address class="contact">
    <p class="contact-row">ABN 48 203 615 772</p>
    <p class="contact-row">Shop 12B 210-218 Harbour Street</p>
    <p class="contact-row">Greenhill NSW 2099 AUSTRALIA</p>
    <p class="contact-row"><span class="contact-label">PO BOX:</span><span>415 Greenhill NSW 2098</span></p>
    <p class="contact-row"><span class="contact-label">Mobile:</span><span>0400 123 456</span></p>
    <p class="contact-row"><span class="contact-label">Phone:</span><span>9000 1234</span></p>
    <p class="contact-row"><span class="contact-label">Fax:</span><span>9000 5678</span></p>
    <p class="contact-row"><span class="contact-label">Email:</span><span>info@nvpre.cc</span></p>
    <p class="contact-row"><span class="contact-label">Website:</span><span>http://nvpre.cc</span></p>
  </address>

  <footer class="member-badge">
    <div class="member-square"></div>
    <div class="member-name">PLVAQT</div>
  </footer>
</div>
</body>
</html>
```